Diagram of Tallowmere’s history for website

This project is to design the attached diagram along the lines of the attached image but in our branding - style guide attached. The diagram will be going on the Tallowmere website - www.tallowmere.au.

```html
<!DOCTYPE html>
<html lang="en">
<head>
<meta charset="utf-8">
<title>Tallowmere – Our History</title>
<link href="https://fonts.googleapis.com/css2?family=Poppins:wght@400;600;700&display=swap" rel="stylesheet">
<style>
  :root{
    --page:#ffffff;
    --ink:#1d1d1b;
    --slate:#6f8496;
    --slate-title:#7d93a5;
    --slate-line:#d6dbe0;
    --slate-bubble:#6e8291;
    --sand-bubble:#d8b89c;
    --sand-line:#8097a9;
    --sand-title:#7b8c87;
    --sand-heading:#1d1d1b;
  }
  *{box-sizing:border-box;margin:0;padding:0}
  html,body{width:1200px;height:849px;overflow:hidden;background:var(--page)}
  .canvas{width:1200px;height:849px;position:relative;overflow:hidden}
  .stage{position:absolute;left:0;top:0;width:2339px;height:1654px;transform:scale(0.513);transform-origin:0 0;
    font-family:"Poppins",sans-serif;color:var(--ink)}
  .timeline{position:absolute;top:0;width:1135px;height:1654px}
  .timeline--slate{left:0;--line:var(--slate-line);--bubble:var(--slate-bubble);--heading:var(--slate);--title:var(--slate-title)}
  .timeline--sand{left:1135px;--line:var(--sand-line);--bubble:var(--sand-bubble);--heading:var(--sand-heading);--title:var(--sand-title)}
  .timeline__path{position:absolute;left:0;top:0;width:1135px;height:1654px}
  .timeline__title{position:absolute;left:167px;top:110px;font-size:31px;font-weight:700;color:var(--title);letter-spacing:0.2px;line-height:40px}
  .timeline__future{position:absolute;left:596px;top:1461px;font-size:31px;font-weight:700;color:var(--title);line-height:40px}
  .milestones{position:absolute;font-size:18.5px;line-height:23.4px;font-weight:400}
  .milestones--left{left:277px;text-align:left}
  .milestones--right{right:290px;text-align:right}
  .milestone + .milestone{margin-top:14px}
  .milestone__title{font-weight:700;color:var(--heading);font-size:19px;letter-spacing:0.1px}
  .milestone__text{white-space:nowrap}
  .bubble__year{font-family:"Poppins",sans-serif;font-weight:700;font-size:26px;fill:var(--ink)}
</style>
</head>
<body>
<div class="canvas">
<div class="stage">

  <!-- Slate colourway -->
  <section class="timeline timeline--slate">
    <svg class="timeline__path" viewBox="0 0 1135 1654" aria-hidden="true">
      <defs>
        <filter id="shadow-a" x="-50%" y="-50%" width="200%" height="200%">
          <feDropShadow dx="6" dy="8" stdDeviation="6" flood-color="#000" flood-opacity="0.22"/>
        </filter>
        <path id="pin-a" d="M-47 0 A47 47 0 0 1 47 0 L47 47 L0 47 A47 47 0 0 1 -47 0 Z"/>
      </defs>
      <g fill="none" stroke="var(--line)" stroke-width="6" stroke-linecap="round" stroke-linejoin="round">
        <circle cx="186" cy="167" r="11"/>
        <path d="M186 178 V320 Q186 350 216 350 H900 Q932 350 932 382 V443 Q932 475 900 475 H216 Q184 475 184 507 V560 Q184 591 216 591 H900 Q932 591 932 623 V684 Q932 716 900 716 H216 Q184 716 184 748 V976 Q184 1008 216 1008 H900 Q932 1008 932 1040 V1328 Q932 1360 900 1360 H216 Q184 1360 184 1392 V1446 Q184 1478 216 1478 H578"/>
        <path d="M566 1466 L578 1478 L566 1490"/>
      </g>
      <g fill="var(--bubble)" filter="url(#shadow-a)">
        <use href="#pin-a" transform="translate(195 247) rotate(-35)"/>
        <use href="#pin-a" transform="translate(918 367) rotate(95)"/>
        <use href="#pin-a" transform="translate(204 482) rotate(-15)"/>
        <use href="#pin-a" transform="translate(918 605) rotate(95)"/>
        <use href="#pin-a" transform="translate(204 735) rotate(-15)"/>
        <use href="#pin-a" transform="translate(918 1025) rotate(95)"/>
      </g>
      <g fill="#fff">
        <circle cx="195" cy="247" r="34"/><circle cx="918" cy="367" r="34"/>
        <circle cx="204" cy="482" r="34"/><circle cx="918" cy="605" r="34"/>
        <circle cx="204" cy="735" r="34"/><circle cx="918" cy="1025" r="34"/>
      </g>
      <g class="bubble__year" text-anchor="middle">
        <text x="195" y="256">2019</text><text x="918" y="376">2018</text>
        <text x="204" y="491">2019</text><text x="918" y="614">2021</text>
        <text x="204" y="744">2022</text><text x="918" y="1034">2023</text>
      </g>
    </svg>

    <h2 class="timeline__title">OUR HISTORY</h2>

    <div class="milestones milestones--left" style="top:172px">
      <div class="milestone">
        <div class="milestone__title">TALLOWMERE COMMENCES</div>
        <div class="milestone__text">Maren started&nbsp; the business with 25 years’ experience&nbsp; working for government<br>&amp; non- government disability &amp;&nbsp; community services.<br>Our first office is in Elmbrook.</div>
      </div>
      <div class="milestone" style="margin-top:8px">
        <div class="milestone__title">NDCS PROVIDER</div>
        <div class="milestone__text">Tallowmere becomes a NDCS Registered provider.</div>
      </div>
    </div>

    <div class="milestones milestones--right" style="top:377px">
      <div class="milestone">
        <div class="milestone__title">CLINIC EXPANSION</div>
        <div class="milestone__text">Tallowmere moves offices twice in Elmbrook due to growth &amp; expansion.<br>Clinic established.</div>
      </div>
    </div>

    <div class="milestones milestones--left" style="top:506px;left:279px">
      <div class="milestone">
        <div class="milestone__title">MOVE TO FERNCLIFF</div>
        <div class="milestone__text" style="margin-top:3px">Tallowmere moves to Ferncliff due to further growth &amp; expansion.</div>
      </div>
    </div>

    <div class="milestones milestones--right" style="top:617px">
      <div class="milestone">
        <div class="milestone__title">FAIR-CORPORATION</div>
        <div class="milestone__text">Tallowmere becomes a accredited Fair-Corporation having met the highest<br>standards of environmental, social &amp; community performance.</div>
      </div>
    </div>

    <div class="milestones milestones--left" style="top:754px;left:279px">
      <div class="milestone">
        <div class="milestone__title">CORVALLA BEST OF BUSINESS</div>
        <div class="milestone__text">Tallowmere wins the Corvalla Best of Business Award (Vic) for building<br>communities.</div>
      </div>
      <div class="milestone">
        <div class="milestone__title">MOVE TO DUNMORE</div>
        <div class="milestone__text">Tallowmere moves to a larger premises in Dunmore .</div>
      </div>
      <div class="milestone">
        <div class="milestone__title">PARTNERSHIPS</div>
        <div class="milestone__text">Partnerships established with Tarawa Learning Centre for Children with Disability &amp;<br>Wirrin Yarra (Eastbank University).</div>
      </div>
    </div>

    <div class="milestones milestones--right" style="top:1038px">
      <div class="milestone">
        <div class="milestone__title">REBRANDING</div>
        <div class="milestone__text">Tallowmere rebranded.</div>
      </div>
      <div class="milestone">
        <div class="milestone__title">RECONCILIATION ACTION PLAN (RAP)</div>
        <div class="milestone__text">Tallowmere’s Reflect RAP developed &amp; endorsed.</div>
      </div>
      <div class="milestone">
        <div class="milestone__title">CLIENT ADVISORY GROUP</div>
        <div class="milestone__text">Tallowmere’s Client Advisory Group commences.</div>
      </div>
      <div class="milestone">
        <div class="milestone__title">E-LEARNING PLATFORM</div>
        <div class="milestone__text">Tallowmere e-learning platform launched.</div>
      </div>
      <div class="milestone">
        <div class="milestone__title">SPECTRUM MARK</div>
        <div class="milestone__text">Tallowmere achieves Spectrum Mark accreditation .</div>
      </div>
    </div>

    <div class="timeline__future">OUR FUTURE</div>
  </section>

  <!-- Sand colourway -->
  <section class="timeline timeline--sand">
    <svg class="timeline__path" viewBox="0 0 1135 1654" aria-hidden="true">
      <defs>
        <filter id="shadow-b" x="-50%" y="-50%" width="200%" height="200%">
          <feDropShadow dx="6" dy="8" stdDeviation="6" flood-color="#000" flood-opacity="0.2"/>
        </filter>
        <path id="pin-b" d="M-47 0 A47 47 0 0 1 47 0 L47 47 L0 47 A47 47 0 0 1 -47 0 Z"/>
      </defs>
      <g fill="none" stroke="var(--line)" stroke-width="6" stroke-linecap="round" stroke-linejoin="round">
        <circle cx="186" cy="167" r="11"/>
        <path d="M186 178 V320 Q186 350 216 350 H900 Q932 350 932 382 V443 Q932 475 900 475 H216 Q184 475 184 507 V560 Q184 591 216 591 H900 Q932 591 932 623 V684 Q932 716 900 716 H216 Q184 716 184 748 V976 Q184 1008 216 1008 H900 Q932 1008 932 1040 V1328 Q932 1360 900 1360 H216 Q184 1360 184 1392 V1446 Q184 1478 216 1478 H578"/>
        <path d="M566 1466 L578 1478 L566 1490"/>
      </g>
      <g fill="var(--bubble)" filter="url(#shadow-b)">
        <use href="#pin-b" transform="translate(195 247) rotate(-35)"/>
        <use href="#pin-b" transform="translate(918 367) rotate(95)"/>
        <use href="#pin-b" transform="translate(204 482) rotate(-15)"/>
        <use href="#pin-b" transform="translate(918 605) rotate(95)"/>
        <use href="#pin-b" transform="translate(204 735) rotate(-15)"/>
        <use href="#pin-b" transform="translate(918 1025) rotate(95)"/>
      </g>
      <g fill="#fff">
        <circle cx="195" cy="247" r="34"/><circle cx="918" cy="367" r="34"/>
        <circle cx="204" cy="482" r="34"/><circle cx="918" cy="605" r="34"/>
        <circle cx="204" cy="735" r="34"/><circle cx="918" cy="1025" r="34"/>
      </g>
      <g class="bubble__year" text-anchor="middle">
        <text x="195" y="256">2019</text><text x="918" y="376">2018</text>
        <text x="204" y="491">2019</text><text x="918" y="614">2021</text>
        <text x="204" y="744">2022</text><text x="918" y="1034">2023</text>
      </g>
    </svg>

    <h2 class="timeline__title">OUR HISTORY</h2>

    <div class="milestones milestones--left" style="top:172px">
      <div class="milestone">
        <div class="milestone__title">TALLOWMERE COMMENCES</div>
        <div class="milestone__text">Maren started&nbsp; the business with 25 years’ experience&nbsp; working for government<br>&amp; non- government disability &amp;&nbsp; community services.<br>Our first office is in Elmbrook.</div>
      </div>
      <div class="milestone" style="margin-top:8px">
        <div class="milestone__title">NDCS PROVIDER</div>
        <div class="milestone__text">Tallowmere becomes a NDCS Registered provider.</div>
      </div>
    </div>

    <div class="milestones milestones--right" style="top:377px">
      <div class="milestone">
        <div class="milestone__title">CLINIC EXPANSION</div>
        <div class="milestone__text">Tallowmere moves offices twice in Elmbrook due to growth &amp; expansion.<br>Clinic established.</div>
      </div>
    </div>

    <div class="milestones milestones--left" style="top:506px;left:279px">
      <div class="milestone">
        <div class="milestone__title">MOVE TO FERNCLIFF</div>
        <div class="milestone__text" style="margin-top:3px">Tallowmere moves to Ferncliff due to further growth &amp; expansion.</div>
      </div>
    </div>

    <div class="milestones milestones--right" style="top:617px">
      <div class="milestone">
        <div class="milestone__title">FAIR-CORPORATION</div>
        <div class="milestone__text">Tallowmere becomes a accredited Fair-Corporation having met the highest<br>standards of environmental, social &amp; community performance.</div>
      </div>
    </div>

    <div class="milestones milestones--left" style="top:754px;left:279px">
      <div class="milestone">
        <div class="milestone__title">CORVALLA BEST OF BUSINESS</div>
        <div class="milestone__text">Tallowmere wins the Corvalla Best of Business Award (Vic) for building<br>communities.</div>
      </div>
      <div class="milestone">
        <div class="milestone__title">MOVE TO DUNMORE</div>
        <div class="milestone__text">Tallowmere moves to a larger premises in Dunmore .</div>
      </div>
      <div class="milestone">
        <div class="milestone__title">PARTNERSHIPS</div>
        <div class="milestone__text">Partnerships established with Tarawa Learning Centre for Children with Disability &amp;<br>Wirrin Yarra (Eastbank University).</div>
      </div>
    </div>

    <div class="milestones milestones--right" style="top:1038px">
      <div class="milestone">
        <div class="milestone__title">REBRANDING</div>
        <div class="milestone__text">Tallowmere rebranded.</div>
      </div>
      <div class="milestone">
        <div class="milestone__title">RECONCILIATION ACTION PLAN (RAP)</div>
        <div class="milestone__text">Tallowmere’s Reflect RAP developed &amp; endorsed.</div>
      </div>
      <div class="milestone">
        <div class="milestone__title">CLIENT ADVISORY GROUP</div>
        <div class="milestone__text">Tallowmere’s Client Advisory Group commences.</div>
      </div>
      <div class="milestone">
        <div class="milestone__title">E-LEARNING PLATFORM</div>
        <div class="milestone__text">Tallowmere e-learning platform launched.</div>
      </div>
      <div class="milestone">
        <div class="milestone__title">SPECTRUM MARK</div>
        <div class="milestone__text">Tallowmere achieves Spectrum Mark accreditation .</div>
      </div>
    </div>

    <div class="timeline__future">OUR FUTURE</div>
  </section>

</div>
</div>
</body>
</html>
```